2 x Digitize Logo | 2 x Business Cards | 2 x Fridge Magnets

We require 6 deliverables:
1. Residential logo redrawn (same just high quality for large print format).
2. Corporate logo redrawn (minor changes to wording and high quality for large print format).
3. New business card design for Furniture Removals (residential)
4. New business card design for Corporate Relocations (business)
5. New Fridge magnet for Furniture removals (residential)
6. New fridge magnet for Corporate Relocations (business)
1. Residential Logo
a. We require the logo to be translated into a high quality digital image with no modifications.
(see attached resilogo.jpg)
2. Residential Logo
a. We require the logo to be edited (add the word corporate relocations) be translated into a high quality digital image.
(see attached corplogo.jpg)
3. Using the resilogo please make a new business card for our business.
a. Please see the web site https://www.bluegatehaulage.com.au for colours and inspiration.
b. The residential business card needs the following information:
i. Business Name (using the residential logo).
ii. Free Call: 1800 BG Haul (the B, G and Haul much be the same colour as the logo).
iii. Website: www.BluegateHaulage.com.au
iv. Address: 4/6 Marlow Court, VIC 3201
v. Email: move@BluegateHaulage.com.au
vi. backof Card:
Review our service
www.TellTallyHub.com.au
Services: Local, Country, Interstate | Furniture Removals | Piano, Billiard Tables & Antiques
4. Using the corplogo please make a new business card for our business.
b. The corporate business card needs the following information:
i. Business Name (using the corporate logo).
v. Email: corporate@BluegateHaulage.com.au
vi. Back of Card:
Review our service
www.TellTallyHub.com.au
Services: Corporate relocations | Office equipment moves | Packing Service | Packing Materials
5. Using the resilogo please make a new fridge magent for our business.
b. The residential fidge magnet needs the following information:
iv. Services: Local, Country, Interstate | Furniture Removals | Piano, Billiard Tables & Antiques
6. Using the corplogo please make a new fridge magent for our business.
b. The corporate fidge magnet needs the following information:
iv. Services: Local, Country, Interstate | Corporate relocations
Target Market(s)
Residential Furniture Removals and Corporate Office relocations
Industry/Entity Type
Business
Contact Information for Business Card
Please see full brief for six items required
Requirements
Must have
- Clean simple, easy to read
Nice to have
- fresh, stand out, eye catching
Should not have
- plain, standard, boring, general

```html
<!DOCTYPE html>
<html lang="en">
<head>
<meta charset="utf-8">
<title>Bluegate Haulage – Business Card</title>
<link rel="stylesheet" href="https://fonts.googleapis.com/css2?family=Open+Sans:ital,wght@0,400;0,600;0,700;0,800;1,400&display=swap">
<style>
  :root {
    --bg: #2b2b2b;
    --card: #1f1f1f;
    --ink: #f2f2f2;
    --yellow: #ffc80a;
    --red: #e8202a;
    --green: #2bb24c;
  }
  * { box-sizing: border-box; margin: 0; padding: 0; }
  html, body { width: 1200px; height: 900px; overflow: hidden; }
  body {
    background: var(--bg);
    font-family: "Open Sans", Arial, sans-serif;
    color: var(--ink);
    display: flex; flex-direction: column; align-items: center; justify-content: center; gap: 36px;
  }
  .card {
    position: relative; width: 720px; height: 400px;
    background: var(--card);
    box-shadow: 0 10px 30px rgba(0,0,0,.45);
    overflow: hidden;
  }
  .stripe { position: absolute; left: 0; right: 0; bottom: 0; height: 14px; display: flex; }
  .stripe span { flex: 1; }
  .stripe .y { background: var(--yellow); }
  .stripe .r { background: var(--red); }
  .stripe .g { background: var(--green); }

  /* back */
  .tag {
    position: absolute; background: var(--green); color: #fff; font-weight: 700;
  }
  .tag-service { left: 40px; top: 30px; width: 112px; padding: 4px 0; text-align: center; font-size: 20px; font-weight: 800; }
  .services { position: absolute; left: 170px; top: 30px; font-size: 15px; font-weight: 700; line-height: 1.4; }
  .review-title { position: absolute; left: 380px; top: 108px; color: var(--yellow); font-weight: 600; font-size: 15px; letter-spacing: .5px; }
  .review { position: absolute; left: 40px; right: 30px; display: flex; gap: 22px; align-items: flex-start; }
  .review .tag { position: static; width: 120px; flex: none; font-size: 16px; padding: 16px 18px; line-height: 1.25; }
  .review p { font-size: 13.2px; line-height: 1.4; }
  .review-1 { top: 140px; }
  .review-2 { top: 238px; }

  /* front */
  .brand { position: absolute; left: 46px; top: 52px; font-size: 46px; font-weight: 800; color: var(--yellow); letter-spacing: .5px; }
  .contacts { position: absolute; left: 46px; bottom: 56px; list-style: none; font-size: 19px; line-height: 1.6; }
  .contacts li { display: flex; align-items: center; gap: 14px; }
  .contacts svg { width: 18px; height: 18px; flex: none; }
  .label { color: var(--green); }
  .bg-b { color: var(--yellow); font-weight: 800; }
  .bg-g { color: var(--red); font-weight: 800; }
  .bg-haul { color: var(--green); font-weight: 800; }
  .address { position: absolute; right: 44px; bottom: 48px; font-size: 20px; line-height: 1.35; }
  .address .label { color: var(--yellow); }
</style>
</head>
<body>

<section class="card card-back">
  <div class="tag tag-service">Service</div>
  <p class="services">Local | Country | Interstate | Furniture Removals<br>Piano | Billiard Tables &amp; Antiques</p>
  <h2 class="review-title">COUSTOMER'S REVIEW</h2>
  <div class="review review-1">
    <div class="tag">Milo</div>
    <p>Well, what can I say? Booking process was easy, information clear and concise. Truck turned up exactly on time, Reid and Owen the right combination of friendly yet professional. Quick and efficient service, very careful with everything, no damage at all. Pricing was very acceptable.</p>
  </div>
  <div class="review review-2">
    <div class="tag">Warren<br>And Jo</div>
    <p>Ted and Owen delivered our new sideboard today, we would like to compliment the company for the efficient, friendly service these two gave us. On the basis of this experience we will not hesitate to use and recommend your company in the future. In short, your refrigerator magnet had gone straight to the pool room!! Thanks from two more satisfied customers.</p>
  </div>
  <div class="stripe"><span class="y"></span><span class="r"></span><span class="g"></span></div>
</section>

<section class="card card-front">
  <h1 class="brand">Bluegate Haulage</h1>
  <ul class="contacts">
    <li>
      <svg viewBox="0 0 24 24" aria-hidden="true"><path fill="#2bb24c" d="M6.6 10.8a15 15 0 0 0 6.6 6.6l2.2-2.2a1 1 0 0 1 1-.25 11.4 11.4 0 0 0 3.6.57 1 1 0 0 1 1 1V20a1 1 0 0 1-1 1A17 17 0 0 1 3 4a1 1 0 0 1 1-1h3.5a1 1 0 0 1 1 1c0 1.25.2 2.45.57 3.57a1 1 0 0 1-.25 1z"/></svg>
      <span><span class="label">Free Call:</span> 1800 <span class="bg-b">B</span> <span class="bg-g">G</span> <span class="bg-haul">Haul</span></span>
    </li>
    <li>
      <svg viewBox="0 0 24 24" aria-hidden="true"><rect x="2" y="5" width="20" height="14" rx="1" fill="#2bb24c"/><path d="M2 6l10 7 10-7" fill="none" stroke="#1f1f1f" stroke-width="2"/></svg>
      <span>move@BluegateHaulage.com.au</span>
    </li>
    <li>
      <svg viewBox="0 0 24 24" aria-hidden="true"><g fill="none" stroke="#2bb24c" stroke-width="2"><circle cx="12" cy="12" r="9"/><ellipse cx="12" cy="12" rx="4" ry="9"/><path d="M3 12h18M5 7h14M5 17h14"/></g></svg>
      <span>www.BluegateHaulage.com.au</span>
    </li>
  </ul>
  <p class="address"><span class="label">Address:</span> 4/6 Marlow<br>Court, VIC 3201</p>
  <div class="stripe"><span class="y"></span><span class="r"></span><span class="g"></span></div>
</section>

</body>
</html>
```